Clear sticker design for packaging

I need 4” diameter clear stickers designed for birthdays, thank you , teachers day and all the other special days to complete my gift packaging. They will go on the top of each tube to differentiate each gift for each occasion. Our design is on craft paper and I’ve uploaded a few examples of what we are trying to achieve. Last picture is the top of our tube where the stickers will be placed. We don’t want too much color unless for Christmas and Valentine’s Day maybe! We are working with black and gold or a mixture of both mostly

```html
<!DOCTYPE html>
<html lang="en">
<head>
<meta charset="utf-8">
<title>Happy Birthday Sticker</title>
<link rel="stylesheet" href="https://fonts.googleapis.com/css2?family=Bungee+Inline&display=swap">
<style>
  :root {
    --paper: #ffffff;
    --ink: #3b3b3b;
    --ink-deep: #111111;
    --ring-outer: #3a3a3a;
    --floral-tone: #d9d9d9;
  }
  html, body {
    margin: 0;
    padding: 0;
    width: 1200px;
    height: 2444px;
    overflow: hidden;
    background: var(--paper);
  }
  .sticker {
    display: block;
    width: 1200px;
    height: 2444px;
  }
  .ring-outer { fill: none; stroke: var(--ring-outer); stroke-width: 4; }
  .ring-inner { fill: none; stroke: var(--ink-deep); stroke-width: 5; }
  .ray { stroke: var(--ink); stroke-width: 9; stroke-linecap: round; fill: none; }
  .star { fill: var(--ink); }
  .greeting {
    font-family: "Bungee Inline", "Arial Black", sans-serif;
    fill: var(--ink);
    text-anchor: middle;
  }
  .greeting-top { font-size: 110px; }
  .greeting-bottom { font-size: 112px; }
  .floral-spray { fill: var(--floral-tone); }
</style>
</head>
<body>
<svg class="sticker" viewBox="0 0 1200 2444" xmlns="http://www.w3.org/2000/svg">
  <g class="badge" transform="translate(600 1222)">
    <circle class="ring-outer" r="452"/>
    <circle class="ring-inner" r="422"/>

    <g class="burst-rays">
      <path class="ray" d="M12 -355 L12 -290"/>
      <path class="ray" d="M-35 -330 L-42 -272"/>
      <path class="ray" d="M58 -330 L50 -272"/>
      <path class="ray" d="M-80 -305 L-95 -262"/>
      <path class="ray" d="M100 -305 L88 -262"/>
      <path class="ray" d="M-115 -270 L-108 -250"/>
    </g>

    <polygon class="star" transform="translate(-292 -196)"
      points="0,-26 7.6,-8 27,-8 11.5,4 17,24 0,12 -17,24 -11.5,4 -27,-8 -7.6,-8"/>
    <polygon class="star" transform="translate(300 -196)"
      points="0,-26 7.6,-8 27,-8 11.5,4 17,24 0,12 -17,24 -11.5,4 -27,-8 -7.6,-8"/>

    <text class="greeting greeting-top" x="4" y="-148" textLength="460" lengthAdjust="spacingAndGlyphs">HAPPY</text>
    <text class="greeting greeting-bottom" x="8" y="-18" textLength="720" lengthAdjust="spacingAndGlyphs">BIRTHDAY</text>

    <ellipse class="floral-spray" role="img" aria-label="Line-drawn floral spray with a five-petal flower and leaves"
      cx="15" cy="200" rx="140" ry="85"/>
  </g>
</svg>
</body>
</html>
```